Premium website for 'Kestrel Voyages Elite'

Exclusive Torque League travel packages: world-class tickets, premium hospitality, seamless travel, and curated experiences that bring the spirit of each destination to life.

1. Overall Style and Impression
Aesthetic: Modern, premium, and dynamic, reflecting the speed and excitement of a high-profile sport or event.

Focus: Highly visual and focused on driving users toward specific, high-value conversion points (like finding a race or viewing a premium package).

We need on the homepage a few blocks for all destinations.
One the specific page of the destination, we need a list of tickets.
An example for our website is https://zomerratours.com/

Functional requirements

The web site is designed to deliver an end-to-end Torque League travel experience, combining flight bookings, hotel reservations, and race ticket purchases into one seamless booking process. This system provides a unified API layer that integrates external booking services and enables developers to build, manage, and customize complete travel packages for each TL Grand Prix event.

System Overview

The platform is built around three core microservices, all connected through a central Package API:

1. Flight Booking Service ✈️
Integrates with global flight providers (e.g.,Flyvora API).

2. Hotel Booking Service 🏨
Connects to hotel aggregator APIs (e.g., Bunkly).
Offers real-time availability, dynamic pricing, and filtering by proximity to TL circuits.

3. Ticket Booking Service 🎟️
Manages TL race ticket inventory and seat categories (Grandstand, VIP, General Admission).

CUSTOMER FEEDBACK
After each booking, a customer will be asked to fill in a questionaire.

CHAT BOT
A chat bot will answer the frequently asked questions.

OUR VISION
We believe life is meant to be lived at full throttle.
Not just seen, but felt. Not just remembered, but relived again and again.

MISSION
That’s why we craft once-in-a-lifetime Torque League journeys — where the roar of the engines meets the soul of the city. Where luxury travel and local culture collide with pure adrenaline. Where you don’t just watch the race… you become part of its story.

PRODUCTS

Target Market(s)

Affluent individuals, typically 35−65 years old, in professional, executive, or entrepreneurial roles. High net worth with significant disposable income.

Coding

Coded - Design and coding required

Number of Pages Required

5+ page

Requirements
Must have
• Central Package API
Nice to have
• Customer feedback after each booking , chat bot.

```html
<!DOCTYPE html>
<html lang="en">
<head>
<meta charset="utf-8">
<title>Kestrel Voyages Elite — Torque League Travel</title>
<link rel="stylesheet" href="https://fonts.googleapis.com/css2?family=Saira:wght@300;500;700;800&family=Poppins:wght@400;500;600;700&display=swap">
<style>
:root{
  --red:#e10600;
  --ink:#111111;
  --panel:#2a2a2c;
  --white:#ffffff;
  --grey-bg:#e9eaec;
  --text-dark:#222;
}
*{box-sizing:border-box;margin:0;padding:0}
html,body{width:1200px;height:4728px;overflow:hidden}
body{font-family:"Poppins",sans-serif;color:var(--white);background:var(--ink)}
h1,h2,h3{font-family:"Saira",sans-serif;text-transform:uppercase}
a{color:inherit;text-decoration:none}
section,header,footer{position:relative;width:1200px;overflow:hidden}

.section-title{font-size:46px;font-weight:700;text-align:center;letter-spacing:1px;line-height:1}
.btn{display:inline-flex;align-items:center;gap:8px;background:var(--red);color:var(--white);font-family:"Poppins",sans-serif;font-weight:600;font-size:13px;text-transform:uppercase;height:42px;padding:0 30px;letter-spacing:.5px;white-space:nowrap}
.btn svg{width:12px;height:12px}
.view-all{position:absolute;left:50%;transform:translateX(-50%)}
.arrow{position:absolute;width:30px;height:30px;border-radius:50%;display:flex;align-items:center;justify-content:center;background:var(--red)}
.arrow.prev{background:#d9d9d9}
.arrow svg{width:12px;height:12px}
.link-more{display:inline-flex;align-items:center;gap:6px;color:var(--red);font-weight:600;font-size:13px;text-transform:uppercase}
.link-more svg{width:11px;height:11px}
.photo{display:block}

/* HERO */
.hero{height:720px;background:linear-gradient(180deg,#0d0d0e 0%,#2b2b2f 30%,#3b1614 55%,#151517 85%,#0d0d0e 100%)}
.hero .photo{position:absolute;inset:0;background:radial-gradient(ellipse at 40% 70%,rgba(170,30,25,.55),transparent 55%),radial-gradient(ellipse at 80% 30%,rgba(120,120,125,.35),transparent 50%)}
.hero::after{content:"";position:absolute;inset:0;background:rgba(0,0,0,.35)}
.nav{position:absolute;top:0;left:0;right:0;height:64px;display:flex;align-items:center;padding:0 100px 0 108px;z-index:2}
.brand{font-family:"Saira",sans-serif;font-weight:700;font-size:20px;color:var(--red);margin-right:auto}
.nav-links{display:flex;gap:36px;font-size:15px;font-weight:500;position:absolute;left:384px}
.nav-icons{display:flex;gap:22px}
.nav-icons svg{width:18px;height:18px}
.hero-content{position:absolute;top:128px;left:0;right:0;text-align:center;z-index:2}
.hero-kicker{font-size:60px;font-weight:300;line-height:1.05}
.hero-title{font-size:72px;font-weight:800;line-height:1}
.hero-sub{font-size:17px;margin:18px 0 24px}
.hero .arrow{top:336px;z-index:2}

/* DARK BLOCKS */
.dark-band{background:linear-gradient(180deg,#0e0e0f 0%,#232325 40%,#1a1a1c 70%,#121213 100%)}
.schedule{height:720px}
.schedule .section-title{position:absolute;top:64px;width:100%}
.card-row{position:absolute;left:108px;display:flex;gap:42px}
.race-card{width:300px;height:400px;background:var(--white);color:var(--text-dark);padding:12px 12px}
.race-card .photo{height:200px;background:linear-gradient(160deg,#2d3444,#6d6f73 55%,#b9b5ad)}
.race-card h3{font-family:"Poppins",sans-serif;text-transform:none;font-size:17px;font-weight:700;margin:16px 0 12px}
.meta{display:flex;align-items:center;gap:12px;font-size:13px;margin-bottom:10px}
.meta i{width:24px;height:24px;border-radius:50%;background:#111;display:flex;align-items:center;justify-content:center}
.meta svg{width:12px;height:12px}
.race-card .link-more{margin-top:10px}

.hospitality{height:732px}
.hospitality .section-title{position:absolute;top:48px;width:100%}
.section-sub{position:absolute;left:0;right:0;text-align:center;font-size:15px;line-height:1.6}
.hosp-row{position:absolute;top:208px;left:108px;display:flex;gap:32px}
.hosp-card{position:relative;width:472px;height:380px}
.hosp-card .panel{position:absolute;inset:0;background:var(--white);clip-path:polygon(18% 0,100% 0,100% 100%,0 100%,0 34%)}
.hosp-card .photo{position:absolute;left:0;top:64px;width:208px;height:230px;background:linear-gradient(150deg,#2b2f3a,#7a7f86 50%,#9e2a22)}
.hosp-card .body{position:absolute;left:232px;top:76px;right:20px;color:var(--text-dark)}
.hosp-card h3{font-family:"Poppins",sans-serif;font-size:17px;font-weight:700;margin-bottom:10px}
.hosp-card p{font-size:15px;line-height:1.5;margin-bottom:16px}

/* TRAVEL */
.travel{height:720px;background:var(--grey-bg);color:var(--text-dark)}
.travel .section-title{position:absolute;top:72px;width:100%}
.map{position:absolute;left:120px;top:176px;width:480px;height:420px;background:radial-gradient(ellipse at 45% 55%,#d4d5d8,#e4e5e8 70%)}
.trip-list{position:absolute;left:672px;top:176px;display:flex;flex-direction:column;gap:20px}
.trip{display:flex;gap:18px;height:128px}
.trip .photo{width:148px;height:128px;background:linear-gradient(160deg,#2e3038,#6b6a6a 60%,#a39a8d)}
.trip h3{font-family:"Poppins",sans-serif;text-transform:none;font-size:20px;font-weight:700;margin:4px 0 6px}
.flag{display:block;width:22px;height:14px;background:#2c4a8a;margin-bottom:4px}
.trip p{font-size:15px;line-height:1.35}
.trip .link-more{margin-top:6px}

/* EXPERIENCES */
.experiences{height:712px}
.experiences .section-title{position:absolute;top:100px;width:100%}
.exp-row{position:absolute;top:170px;left:112px;display:flex;gap:42px}
.exp-card{width:296px;height:396px;background:var(--white);color:var(--text-dark);padding:12px}
.exp-card.featured{background:var(--panel);color:var(--white)}
.exp-card .photo{height:210px;background:linear-gradient(160deg,#1f2a45,#8a2c25 55%,#c8c2b6)}
.exp-card h3{font-family:"Poppins",sans-serif;text-transform:none;font-size:20px;font-weight:700;margin:18px 0 6px}
.exp-card p{font-size:16px;line-height:1.4;margin-bottom:8px}

/* TICKETS FORM */
.tickets{height:560px}
.tickets .section-title{position:absolute;top:84px;width:100%}
.ticket-form{position:absolute;left:272px;top:144px;width:656px;display:grid;grid-template-columns:1fr 1fr;gap:12px 16px}
.field{height:44px;background:var(--white);color:#333;display:flex;align-items:center;gap:12px;padding:0 14px;font-size:14px}
.field svg{width:14px;height:14px;flex:none}
.field .caret{margin-left:auto}
.field.message{grid-column:1/3;height:104px;align-items:flex-start;padding-top:12px}
.ticket-form .btn{grid-column:1/3;justify-self:center;margin-top:24px}

/* FOOTER */
.site-footer{height:568px;background:#0c0c0d}
.footer-cols{position:absolute;top:48px;left:108px;right:100px;display:grid;grid-template-columns:276px 292px 216px 1fr}
.footer-cols .brand{font-size:18px;color:var(--white);display:block;margin-bottom:26px}
.footer-about{font-size:14px;line-height:1.6;color:#cfcfcf;width:200px}
.socials{display:flex;gap:10px;margin-top:22px}
.socials span{width:26px;height:26px;border-radius:50%;background:var(--red)}
.footer-col h4{font-family:"Saira",sans-serif;font-weight:700;font-size:16px;text-transform:uppercase;margin-bottom:26px;padding-top:6px}
.footer-col li{list-style:none;font-size:13px;color:#cfcfcf;margin-bottom:26px}
.contact li{display:flex;align-items:center;gap:12px}
.contact svg{width:14px;height:14px}
.footer-bottom{position:absolute;left:108px;right:100px;bottom:40px;display:flex;font-size:13px;color:#cfcfcf}
.footer-bottom .legal{margin-left:auto;display:flex;gap:36px}
.footer-bottom b{color:var(--red);font-weight:500}
</style>
</head>
<body>

<header class="hero">
  <div class="photo" role="img" aria-label="Open-wheel race cars racing along a grandstand straight"></div>
  <nav class="nav">
    <a class="brand" href="#">Kestrel Voyages Elite</a>
    <div class="nav-links"><a href="#">Tickets</a><a href="#">Hospitality</a><a href="#">Travel</a><a href="#">Experiences</a><a href="#">Contact</a></div>
    <div class="nav-icons">
      <svg viewBox="0 0 24 24" fill="none" stroke="#fff" stroke-width="2"><path d="M22 16.9v3a2 2 0 0 1-2.2 2 19.8 19.8 0 0 1-8.6-3.1 19.5 19.5 0 0 1-6-6A19.8 19.8 0 0 1 2.1 4.2 2 2 0 0 1 4.1 2h3a2 2 0 0 1 2 1.7c.1.9.4 1.8.7 2.7a2 2 0 0 1-.5 2.1L8 9.8a16 16 0 0 0 6 6l1.3-1.3a2 2 0 0 1 2.1-.4c.9.3 1.8.6 2.7.7a2 2 0 0 1 1.7 2z"/></svg>
      <svg viewBox="0 0 24 24" fill="none" stroke="#fff" stroke-width="2"><circle cx="12" cy="8" r="4"/><path d="M4 21c0-4 4-6 8-6s8 2 8 6"/></svg>
      <svg viewBox="0 0 24 24" fill="none" stroke="#fff" stroke-width="2"><path d="M5 8h14l-1 13H6z"/><path d="M9 8V6a3 3 0 0 1 6 0v2"/></svg>
    </div>
  </nav>
  <div class="hero-content">
    <h1><span class="hero-kicker" style="display:block">Offers Premium</span><span class="hero-title">Grandstand Tickets</span></h1>
    <p class="hero-sub">Many desktop publishing packages and web page editors now use</p>
    <a class="btn" href="#">View Tickets <svg viewBox="0 0 12 12" fill="none" stroke="#fff" stroke-width="2"><path d="M1 6h9M7 3l3 3-3 3"/></svg></a>
  </div>
  <a class="arrow prev" style="left:52px" href="#"><svg viewBox="0 0 12 12" fill="none" stroke="#111" stroke-width="2"><path d="M8 2 4 6l4 4"/></svg></a>
  <a class="arrow" style="left:1116px" href="#"><svg viewBox="0 0 12 12" fill="none" stroke="#fff" stroke-width="2"><path d="M4 2l4 4-4 4"/></svg></a>
</header>

<div class="dark-band">
<section class="schedule">
  <h2 class="section-title">2025 Torque League Schedule</h2>
  <div class="card-row" style="top:152px">
    <article class="race-card">
      <div class="photo" role="img" aria-label="Floodlit circuit straight at night"></div>
      <h3>Lorem Ipsum is simply</h3>
      <div class="meta"><i><svg viewBox="0 0 12 12" fill="#fff"><path d="M6 0a4 4 0 0 0-4 4c0 3 4 8 4 8s4-5 4-8a4 4 0 0 0-4-4zm0 5.5A1.5 1.5 0 1 1 6 2.5a1.5 1.5 0 0 1 0 3z"/></svg></i>Mexico City,Mexico</div>
      <div class="meta"><i><svg viewBox="0 0 12 12" fill="none" stroke="#fff" stroke-width="1.5"><circle cx="6" cy="6" r="4.5"/><path d="M6 3.5V6l2 1"/></svg></i>16-18 oct</div>
      <a class="link-more" href="#">View Details <svg viewBox="0 0 12 12" fill="none" stroke="currentColor" stroke-width="2"><path d="M1 6h9M7 3l3 3-3 3"/></svg></a>
    </article>
    <article class="race-card">
      <div class="photo" role="img" aria-label="Circuit with grandstands at sunset"></div>
      <h3>Lorem Ipsum is simply</h3>
      <div class="meta"><i><svg viewBox="0 0 12 12" fill="#fff"><path d="M6 0a4 4 0 0 0-4 4c0 3 4 8 4 8s4-5 4-8a4 4 0 0 0-4-4zm0 5.5A1.5 1.5 0 1 1 6 2.5a1.5 1.5 0 0 1 0 3z"/></svg></i>Mexico City,Mexico</div>
      <div class="meta"><i><svg viewBox="0 0 12 12" fill="none" stroke="#fff" stroke-width="1.5"><circle cx="6" cy="6" r="4.5"/><path d="M6 3.5V6l2 1"/></svg></i>16-18 oct</div>
      <a class="link-more" href="#">View Details <svg viewBox="0 0 12 12" fill="none" stroke="currentColor" stroke-width="2"><path d="M1 6h9M7 3l3 3-3 3"/></svg></a>
    </article>
    <article class="race-card">
      <div class="photo" role="img" aria-label="Pit lane and paddock buildings"></div>
      <h3>Lorem Ipsum is simply</h3>
      <div class="meta"><i><svg viewBox="0 0 12 12" fill="#fff"><path d="M6 0a4 4 0 0 0-4 4c0 3 4 8 4 8s4-5 4-8a4 4 0 0 0-4-4zm0 5.5A1.5 1.5 0 1 1 6 2.5a1.5 1.5 0 0 1 0 3z"/></svg></i>Mexico City,Mexico</div>
      <div class="meta"><i><svg viewBox="0 0 12 12" fill="none" stroke="#fff" stroke-width="1.5"><circle cx="6" cy="6" r="4.5"/><path d="M6 3.5V6l2 1"/></svg></i>16-18 oct</div>
      <a class="link-more" href="#">View Details <svg viewBox="0 0 12 12" fill="none" stroke="currentColor" stroke-width="2"><path d="M1 6h9M7 3l3 3-3 3"/></svg></a>
    </article>
  </div>
  <a class="arrow prev" style="left:52px;top:336px" href="#"><svg viewBox="0 0 12 12" fill="none" stroke="#111" stroke-width="2"><path d="M8 2 4 6l4 4"/></svg></a>
  <a class="arrow" style="left:1116px;top:336px" href="#"><svg viewBox="0 0 12 12" fill="none" stroke="#fff" stroke-width="2"><path d="M4 2l4 4-4 4"/></svg></a>
  <a class="btn view-all" style="top:616px" href="#">View All <svg viewBox="0 0 12 12" fill="none" stroke="#fff" stroke-width="2"><path d="M1 6h9M7 3l3 3-3 3"/></svg></a>
</section>

<section class="hospitality">
  <h2 class="section-title">Premium Hospitality</h2>
  <p class="section-sub" style="top:108px">Many desktop publishing packages and web page editors now use Lorem Ipsum<br>as their default model text, and a search for 'lorem ipsum' will uncover</p>
  <div class="hosp-row">
    <article class="hosp-card">
      <div class="panel"></div>
      <div class="photo" role="img" aria-label="Race car in the garage with team crew"></div>
      <div class="body">
        <h3>LOREM IPSUM IS SIMPLY</h3>
        <p>Many desktop publishing packages and web page editors now use</p>
        <a class="btn" style="height:36px;padding:0 18px;font-size:12px" href="#">Choose Race <svg viewBox="0 0 12 12" fill="none" stroke="#fff" stroke-width="2"><path d="M1 6h9M7 3l3 3-3 3"/></svg></a>
      </div>
    </article>
    <article class="hosp-card">
      <div class="panel"></div>
      <div class="photo" role="img" aria-label="Red race car on track"></div>
      <div class="body">
        <h3>LOREM IPSUM IS SIMPLY</h3>
        <p>Many desktop publishing packages and web page editors now use</p>
        <a class="btn" style="height:36px;padding:0 18px;font-size:12px" href="#">Choose Race <svg viewBox="0 0 12 12" fill="none" stroke="#fff" stroke-width="2"><path d="M1 6h9M7 3l3 3-3 3"/></svg></a>
      </div>
    </article>
  </div>
  <a class="arrow prev" style="left:52px;top:384px" href="#"><svg viewBox="0 0 12 12" fill="none" stroke="#111" stroke-width="2"><path d="M8 2 4 6l4 4"/></svg></a>
  <a class="arrow" style="left:1116px;top:384px" href="#"><svg viewBox="0 0 12 12" fill="none" stroke="#fff" stroke-width="2"><path d="M4 2l4 4-4 4"/></svg></a>
  <a class="btn view-all" style="top:628px" href="#">View All <svg viewBox="0 0 12 12" fill="none" stroke="#fff" stroke-width="2"><path d="M1 6h9M7 3l3 3-3 3"/></svg></a>
</section>
</div>

<section class="travel">
  <h2 class="section-title">Seamless Travel</h2>
  <div class="map" role="img" aria-label="Circuit layout map with the host country highlighted and route labels"></div>
  <div class="trip-list">
    <article class="trip">
      <div class="photo" role="img" aria-label="Aircraft cabin interior"></div>
      <div><h3>Lorem Ipsum is simply</h3><span class="flag"></span><p>Mexico City,Mexico<br>€3,480</p><a class="link-more" href="#">Read More <svg viewBox="0 0 12 12" fill="none" stroke="currentColor" stroke-width="2"><path d="M1 6h9M7 3l3 3-3 3"/></svg></a></div>
    </article>
    <article class="trip">
      <div class="photo" role="img" aria-label="Paddock walkway"></div>
      <div><h3>Lorem Ipsum is simply</h3><span class="flag" style="background:#c8102e"></span><p>Mexico City,Mexico<br>€3,480</p><a class="link-more" href="#">Read More <svg viewBox="0 0 12 12" fill="none" stroke="currentColor" stroke-width="2"><path d="M1 6h9M7 3l3 3-3 3"/></svg></a></div>
    </article>
    <article class="trip">
      <div class="photo" role="img" aria-label="Race car on the grid"></div>
      <div><h3>Lorem Ipsum is simply</h3><span class="flag" style="background:#3c3b6e"></span><p>Mexico City,Mexico<br>€3,480</p><a class="link-more" href="#">Read More <svg viewBox="0 0 12 12" fill="none" stroke="currentColor" stroke-width="2"><path d="M1 6h9M7 3l3 3-3 3"/></svg></a></div>
    </article>
  </div>
  <a class="btn view-all" style="top:640px" href="#">View All <svg viewBox="0 0 12 12" fill="none" stroke="#fff" stroke-width="2"><path d="M1 6h9M7 3l3 3-3 3"/></svg></a>
</section>

<div class="dark-band">
<section class="experiences">
  <h2 class="section-title">Curated Experiences</h2>
  <div class="exp-row">
    <article class="exp-card">
      <div class="photo" role="img" aria-label="Team crew gathered in the pit lane"></div>
      <h3>Lorem Ipsum is simply</h3><p>Many desktop publishing packages and web page</p>
      <a class="link-more" href="#">Read More <svg viewBox="0 0 12 12" fill="none" stroke="currentColor" stroke-width="2"><path d="M1 6h9M7 3l3 3-3 3"/></svg></a>
    </article>
    <article class="exp-card featured">
      <div class="photo" role="img" aria-label="Podium celebration with crowd"></div>
      <h3>Lorem Ipsum is simply</h3><p>Many desktop publishing packages and web</p>
      <a class="link-more" href="#">Read More <svg viewBox="0 0 12 12" fill="none" stroke="currentColor" stroke-width="2"><path d="M1 6h9M7 3l3 3-3 3"/></svg></a>
    </article>
    <article class="exp-card">
      <div class="photo" role="img" aria-label="Team members celebrating in the garage"></div>
      <h3>Lorem Ipsum is simply</h3><p>Many desktop publishing packages and web page</p>
      <a class="link-more" href="#">Read More <svg viewBox="0 0 12 12" fill="none" stroke="currentColor" stroke-width="2"><path d="M1 6h9M7 3l3 3-3 3"/></svg></a>
    </article>
  </div>
  <a class="arrow prev" style="left:52px;top:352px" href="#"><svg viewBox="0 0 12 12" fill="none" stroke="#111" stroke-width="2"><path d="M8 2 4 6l4 4"/></svg></a>
  <a class="arrow" style="left:1116px;top:352px" href="#"><svg viewBox="0 0 12 12" fill="none" stroke="#fff" stroke-width="2"><path d="M4 2l4 4-4 4"/></svg></a>
  <a class="btn view-all" style="top:612px" href="#">View All <svg viewBox="0 0 12 12" fill="none" stroke="#fff" stroke-width="2"><path d="M1 6h9M7 3l3 3-3 3"/></svg></a>
</section>

<section class="tickets">
  <h2 class="section-title">Get Tickets Now</h2>
  <form class="ticket-form">
    <label class="field"><svg viewBox="0 0 24 24" fill="#111"><circle cx="12" cy="8" r="5"/><path d="M3 22c0-5 4-8 9-8s9 3 9 8z"/></svg>First Name</label>
    <label class="field"><svg viewBox="0 0 24 24" fill="#111"><circle cx="12" cy="8" r="5"/><path d="M3 22c0-5 4-8 9-8s9 3 9 8z"/></svg>Last Name</label>
    <label class="field"><svg viewBox="0 0 24 24" fill="#111"><path d="M2 5h20v14H2z"/><path d="M2 5l10 8 10-8" stroke="#fff" stroke-width="2" fill="none"/></svg>Email</label>
    <label class="field"><svg viewBox="0 0 24 24" fill="#111"><path d="M22 16.9v3a2 2 0 0 1-2.2 2 19.8 19.8 0 0 1-8.6-3.1 19.5 19.5 0 0 1-6-6A19.8 19.8 0 0 1 2.1 4.2 2 2 0 0 1 4.1 2h3a2 2 0 0 1 2 1.7l.7 2.7-1.8 3.4a16 16 0 0 0 6 6l3.4-1.8 2.7.7a2 2 0 0 1 1.9 2.2z"/></svg>Phone</label>
    <label class="field"><svg viewBox="0 0 24 24" fill="#111"><path d="M3 5h18v16H3z"/><path d="M3 10h18" stroke="#fff" stroke-width="2"/></svg>Event</label>
    <label class="field"><svg viewBox="0 0 24 24" fill="#111"><circle cx="9" cy="8" r="4"/><circle cx="17" cy="9" r="3"/><path d="M1 21c0-4 4-7 8-7s8 3 8 7zM15 14c4 0 8 2 8 7h-5"/></svg>No Of People<svg class="caret" viewBox="0 0 12 12" fill="none" stroke="#111" stroke-width="2"><path d="M2 4l4 4 4-4"/></svg></label>
    <label class="field message"><svg viewBox="0 0 24 24" fill="#111"><path d="M2 3h20v14H8l-6 5z"/></svg>Message</label>
    <button class="btn" type="button" style="border:0">Submit Now <svg viewBox="0 0 12 12" fill="none" stroke="#fff" stroke-width="2"><path d="M1 6h9M7 3l3 3-3 3"/></svg></button>
  </form>
</section>
</div>

<footer class="site-footer">
  <div class="footer-cols">
    <div>
      <span class="brand">Kestrel Voyages Elite</span>
      <p class="footer-about">Lorem Ipsum has been the industry's standard dummy text ever since the 1500s.</p>
      <div class="socials"><span></span><span></span><span></span></div>
    </div>
    <div class="footer-col"><h4>Tickets</h4><ul><li>Official TL Tickets</li><li>TL Experiences Ticket Packages</li><li>Torque League Paddock Club</li><li>TL Corporate Hospitality</li></ul></div>
    <div class="footer-col"><h4>Experience</h4><ul><li>Lorem Ipsum</li><li>Lorem Ipsum</li><li>Lorem Ipsum</li><li>Lorem Ipsum</li></ul></div>
    <div class="footer-col contact"><h4>Contact</h4><ul>
      <li><svg viewBox="0 0 24 24" fill="#fff"><path d="M22 16.9v3a2 2 0 0 1-2.2 2 19.8 19.8 0 0 1-8.6-3.1 19.5 19.5 0 0 1-6-6A19.8 19.8 0 0 1 2.1 4.2 2 2 0 0 1 4.1 2h3a2 2 0 0 1 2 1.7l.7 2.7-1.8 3.4a16 16 0 0 0 6 6l3.4-1.8 2.7.7a2 2 0 0 1 1.9 2.2z"/></svg>+44 (0)20 7946 0381</li>
      <li><svg viewBox="0 0 24 24" fill="#fff"><path d="M2 5h20v14H2z"/><path d="M2 5l10 8 10-8" stroke="#0c0c0d" stroke-width="2" fill="none"/></svg>hello@kestrelvoyages.com</li>
    </ul></div>
  </div>
  <div class="footer-bottom">
    <span>© 2025 <b>KESTREL VOYAGES ELITE</b>. All rights reserved</span>
    <div class="legal"><a href="#">Privacy Policy</a><a href="#">Cookies Policy</a><a href="#">Legal Notices</a></div>
  </div>
</footer>

</body>
</html>
```